Personal website: Intro to a software engineer, filmmaker, entrepreneur

I'm looking to do a redesign of my website. It's had many forms over the years, primarily because it's been hard to pin down all what I want to communicate. I'm a software engineer, filmmaker, writer, and entrepreneur. I'm looking to showcase not only what I've done and what I can do, but also who I am, what I'm interested in, and what I have to say. The minimal content at this point would be: Name, photo of me, short intro, publications on Tessary (title, description, date), and social links. In the future I could see adding notable projects, open source contributions, and possibly skills. Think of it as an intro to Dane Holpvist.

I would like this to be all on one page. If I were to pin down the design atheistic I'm going for it would be: Warm, sophisticated, simple, clear, minimal, creative, flat, thoughtful, artistic, and soft. I imagine typography taking more over a role here than images. I know a lot of design is image focused, but I'd rather any photos be accents than main content.

I'm more than happy to give more details if more is needed/wanted.
Updates

Designs look the same

Target Market(s)

Fellow co-creators

Number of Pages Required

1 page

Requirements
Must have
• Name, photo of me, short intro, publications on Tessary (title, description, date), and social links.
Nice to have
• Notable projects, open source contributions, and skills
Should not have
• It should not be overly techy. I'm about building solutions and sharing ideas.
• Should not look corporate.

```html
<!DOCTYPE html>
<html lang="en">
<head>
<meta charset="utf-8">
<title>Dane Holpvist</title>
<link href="https://fonts.googleapis.com/css2?family=Oswald:wght@300;400;500&family=Great+Vibes&family=Josefin+Sans:wght@300;400&family=Open+Sans:wght@400;600&display=swap" rel="stylesheet">
<style>
:root{
  --orange:#e8701f;
  --ink:#1f1f1f;
  --text:#555;
  --muted:#888;
  --ghost:#cfcfcf;
  --panel:#f2f2f2;
  --white:#fff;
  --footer:#161616;
  --green:#4cbb2f;
}
*{margin:0;padding:0;box-sizing:border-box}
html,body{width:1200px;height:3571px;overflow:hidden;background:var(--white)}
body{position:relative;font-family:'Josefin Sans',sans-serif;color:var(--text)}
.abs{position:absolute}
section,header,footer{position:absolute;left:0;width:1200px}

/* hero */
.hero{top:0;height:600px;background:linear-gradient(180deg,#4a4030 0%,#7a6440 35%,#3b3020 70%,#1c170f 100%)}
.hero-photo{position:absolute;inset:0;background:radial-gradient(circle at 70% 30%,rgba(240,210,150,.75),rgba(120,90,50,0) 45%)}
.logo{left:98px;top:44px;font:500 31px/1.2 'Oswald',sans-serif;color:var(--white);letter-spacing:.5px}
.nav-item{top:56px;font:400 16px/1.2 'Oswald',sans-serif;color:var(--white);text-transform:uppercase;white-space:nowrap}
.nav-item.active{color:var(--orange)}
.search{left:1086px;top:59px}
.hero-title{left:652px;top:176px;font:300 64px/76px 'Oswald',sans-serif;color:var(--white);white-space:nowrap}
.dots{left:566px;top:522px;display:flex;gap:5px}
.dots i{width:12px;height:12px;border:2px solid var(--white);border-radius:50%}
.dots i.on{background:var(--white)}

/* headings */
.ghost{font:500 62px/1 'Oswald',sans-serif;color:var(--ghost);text-transform:uppercase;letter-spacing:4px;white-space:nowrap}
.script{font:400 58px/1 'Great Vibes',cursive;color:var(--ink);white-space:nowrap}
.center{left:0;width:1200px;text-align:center}

/* about */
.about{top:600px;height:560px}
.about p{left:98px;top:212px;width:560px;font-size:15px;line-height:33px}
.social{display:flex;gap:10px}
.social span{width:50px;height:50px;border:2px solid var(--orange);border-radius:50%;display:flex;align-items:center;justify-content:center;font:600 10px 'Open Sans',sans-serif;color:var(--orange)}
.portrait-ring{left:736px;top:95px;width:362px;height:362px;border:3px solid var(--orange);border-radius:50%}
.portrait{left:755px;top:114px;width:324px;height:324px;border-radius:50%;background:radial-gradient(circle at 50% 45%,#6a5a50,#3a3330 70%)}

/* publications */
.pubs{top:1160px;height:769px;background:var(--panel)}
.card{top:240px;width:316px;height:447px;background:var(--white);box-shadow:0 1px 4px rgba(0,0,0,.15)}
.card .thumb{height:233px}
.card h3{margin:24px 18px 0;font:400 21px 'Oswald',sans-serif;color:var(--ink)}
.card .date{margin:8px 18px 0;font:400 13px 'Open Sans',sans-serif;color:var(--muted);display:flex;align-items:center;gap:8px}
.card p{margin:12px 18px 0;font-size:14px;line-height:24px}
.arrow{top:448px;width:44px;height:44px;border:2px solid #999;border-radius:50%;display:flex;align-items:center;justify-content:center}

/* contributions */
.contrib{top:1929px;height:802px}
.years{left:144px;top:218px;width:914px;height:86px}
.years .line{position:absolute;left:40px;right:40px;top:42px;height:2px;background:#999}
.year{position:absolute;top:0;width:82px;height:82px;border:2px solid #888;border-radius:50%;background:var(--white);display:flex;align-items:center;justify-content:center;font:400 18px 'Open Sans',sans-serif;color:#444}
.year.on{background:var(--orange);border-color:var(--orange);color:var(--white)}
.tl-line{left:599px;top:371px;width:2px;height:331px;background:#ccc}
.tl-dot{width:16px;height:16px;border-radius:50%;background:var(--orange)}
.tl-month{font:400 20px 'Oswald',sans-serif;color:var(--ink)}
.tl-note{font-size:14px;color:#666}
.tl-head{font:400 15px 'Oswald',sans-serif;color:var(--ink)}
.tl-row{font-size:14px;color:#666}
.bar{height:6px;background:var(--green);border-radius:3px}

/* skills */
.skills{top:2731px;height:562px;background:var(--panel)}
.skill{top:200px;width:340px}
.skill .icon{display:block;height:80px}
.skill h3{margin-top:30px;font:400 25px 'Oswald',sans-serif;color:var(--ink)}
.skill p{margin-top:20px;font-size:14px;line-height:24px;color:#666}

/* footer */
.footer{top:3293px;height:278px;background:var(--footer);color:#ddd}
.footer .social{left:486px;top:48px;gap:8px}
.footer .social span{border-color:#fff;color:#fff}
.contact{top:134px;font:400 15px 'Open Sans',sans-serif}
.links{top:174px;font:400 14px 'Open Sans',sans-serif}
.copy{top:210px;font:400 14px 'Open Sans',sans-serif}
</style>
</head>
<body>

<header class="hero">
  <div class="hero-photo" role="img" aria-label="Silhouette of a filmmaker with a camera on a tripod in a field at sunset"></div>
  <div class="abs logo">DANE HOLPVIST</div>
  <nav>
    <span class="abs nav-item active" style="left:433px">Home</span>
    <span class="abs nav-item" style="left:512px">About me</span>
    <span class="abs nav-item" style="left:623px">Projects</span>
    <span class="abs nav-item" style="left:730px">Contributions</span>
    <span class="abs nav-item" style="left:878px">Skills</span>
    <span class="abs nav-item" style="left:964px">Contact us</span>
  </nav>
  <svg class="abs search" width="18" height="18" viewBox="0 0 18 18"><circle cx="7" cy="7" r="5.5" fill="none" stroke="#fff" stroke-width="2.2"/><line x1="11" y1="11" x2="16" y2="16" stroke="#fff" stroke-width="2.6"/></svg>
  <h1 class="abs hero-title">A collection of<br>my thoughts on tech<br>and current events</h1>
  <div class="abs dots"><i class="on"></i><i></i><i></i><i></i></div>
</header>

<section class="about">
  <div class="abs ghost" style="left:96px;top:98px">Dane Holpvist</div>
  <div class="abs script" style="left:150px;top:106px">Dane Holpvist</div>
  <p class="abs">Nemo enim ipsam voluptatem quia voluptas sit aspernatur aut odit aut fugit, sed quia consequuntur magni dolores eos qui ratione voluptatem sequi nesciunt. Neque porro quisquam est, qui dolorem ipsum quia dolor sit amet, consectetur, adipisci velit, sed quia non numquam eius modi tempora incidunt ut labore et dolore magnam aliquam quaerat luptate tenim ad minimo veniam, quis nostrum.</p>
  <div class="abs social" style="left:99px;top:395px">
    <span>Chirp</span><span>Netwk</span><span>Repo</span>
    <span><svg width="20" height="14" viewBox="0 0 20 14"><rect x="1" y="1" width="18" height="12" rx="2" fill="var(--orange)"/><path d="M1 2l9 6 9-6" fill="none" stroke="#fff" stroke-width="1.5"/></svg></span>
  </div>
  <div class="abs portrait-ring"></div>
  <div class="abs portrait" role="img" aria-label="Portrait photo of Dane Holpvist"></div>
</section>

<section class="pubs">
  <div class="abs ghost center" style="top:100px">Publications</div>
  <div class="abs script center" style="top:112px">Our Projects</div>
  <div class="abs arrow" style="left:28px"><svg width="12" height="16" viewBox="0 0 12 16"><path d="M9 2L3 8l6 6" fill="none" stroke="#888" stroke-width="2"/></svg></div>
  <div class="abs arrow" style="left:1128px"><svg width="12" height="16" viewBox="0 0 12 16"><path d="M3 2l6 6-6 6" fill="none" stroke="#888" stroke-width="2"/></svg></div>

  <article class="abs card" style="left:98px">
    <div class="thumb" role="img" aria-label="Hands holding a video camera rig" style="background:linear-gradient(135deg,#3a4550,#7a6a5a)"></div>
    <h3>Finibus Bonorumet Malorum</h3>
    <div class="date"><svg width="13" height="13" viewBox="0 0 13 13"><rect x="1" y="2" width="11" height="10" fill="var(--orange)"/><rect x="2.5" y="5" width="8" height="5.5" fill="#fff"/></svg>04/09/2018</div>
    <p>Nemo enim ipsam voluptatem quia volupt as sit aspernatur aut odit aut fugit, sequia consequuntur magni dolores eos qui ratione voluptatem sequi nesciunt.</p>
  </article>
  <article class="abs card" style="left:441px">
    <div class="thumb" role="img" aria-label="Hands typing code on a laptop" style="background:linear-gradient(135deg,#1d2a38,#4a5a6a)"></div>
    <h3>Finibus Bonorumet Malorum</h3>
    <div class="date"><svg width="13" height="13" viewBox="0 0 13 13"><rect x="1" y="2" width="11" height="10" fill="var(--orange)"/><rect x="2.5" y="5" width="8" height="5.5" fill="#fff"/></svg>04/09/2018</div>
    <p>Nemo enim ipsam voluptatem quia volupt as sit aspernatur aut odit aut fugit, sequia consequuntur magni dolores eos qui ratione voluptatem sequi nesciunt.</p>
  </article>
  <article class="abs card" style="left:785px">
    <div class="thumb" role="img" aria-label="Team meeting around a laptop on a table" style="background:linear-gradient(135deg,#8a8f95,#d8d6cf)"></div>
    <h3>Finibus Bonorumet Malorum</h3>
    <div class="date"><svg width="13" height="13" viewBox="0 0 13 13"><rect x="1" y="2" width="11" height="10" fill="var(--orange)"/><rect x="2.5" y="5" width="8" height="5.5" fill="#fff"/></svg>04/09/2018</div>
    <p>Nemo enim ipsam voluptatem quia volupt as sit aspernatur aut odit aut fugit, sequia consequuntur magni dolores eos qui ratione voluptatem sequi nesciunt.</p>
  </article>
</section>

<section class="contrib">
  <div class="abs ghost center" style="top:90px">Contributions</div>
  <div class="abs script center" style="top:100px">Open Source Contributions</div>
  <div class="abs years">
    <div class="line"></div>
    <div class="year" style="left:0">2009</div>
    <div class="year" style="left:92px">2010</div>
    <div class="year" style="left:184px">2011</div>
    <div class="year" style="left:276px">2012</div>
    <div class="year" style="left:368px">2013</div>
    <div class="year on" style="left:460px">2014</div>
    <div class="year" style="left:552px">2015</div>
    <div class="year" style="left:644px">2016</div>
    <div class="year" style="left:736px">2017</div>
    <div class="year" style="left:828px">2018</div>
  </div>
  <div class="abs tl-line"></div>
  <div class="abs tl-dot" style="left:592px;top:380px"></div>
  <div class="abs tl-month" style="left:645px;top:366px">December 2014</div>
  <div class="abs tl-note" style="left:645px;top:404px">dholpvist had no activity during this period.</div>

  <div class="abs tl-dot" style="left:592px;top:484px"></div>
  <div class="abs tl-month" style="left:252px;width:300px;text-align:right;top:468px">October 2014</div>
  <div class="abs tl-head" style="left:252px;width:300px;text-align:right;top:512px">Created 10 commits in 2 repositories</div>
  <div class="abs bar" style="left:228px;top:556px;width:84px"></div>
  <div class="abs tl-row" style="left:252px;width:300px;text-align:right;top:548px">dholpvist/recall-reactjs 5 commits</div>
  <div class="abs bar" style="left:228px;top:589px;width:84px"></div>
  <div class="abs tl-row" style="left:252px;width:300px;text-align:right;top:581px">dholpvist/recall 5 commits</div>
  <div class="abs tl-head" style="left:252px;width:300px;text-align:right;top:632px">Created 1 repositories</div>
  <div class="abs tl-dot" style="left:297px;top:667px;width:13px;height:13px"></div>
  <div class="abs tl-row" style="left:252px;width:300px;text-align:right;top:664px">JavaScript&nbsp;&nbsp;&nbsp;&nbsp;&nbsp;&nbsp;dholpvist/recall-reactjs</div>
</section>

<section class="skills">
  <div class="abs ghost center" style="top:84px">Skills</div>
  <div class="abs script center" style="top:94px">Skills</div>
  <div class="abs skill" style="left:98px">
    <svg class="icon" width="84" height="80" viewBox="0 0 84 80"><rect x="0" y="2" width="84" height="56" rx="5" fill="var(--orange)"/><rect x="7" y="9" width="70" height="38" fill="var(--panel)"/><rect x="34" y="58" width="16" height="10" fill="var(--orange)"/><rect x="22" y="68" width="40" height="6" rx="2" fill="var(--orange)"/></svg>
    <h3>Software Engineer</h3>
    <p>Temporibus autem quibusdam et aut officiis deb itis aut re rum necessitatibus saepe eveniet ut vo luptates repuian dae sint et molestiae non rcusa ndae nostrum exerci.</p>
  </div>
  <div class="abs skill" style="left:445px">
    <svg class="icon" width="84" height="80" viewBox="0 0 84 80"><rect x="0" y="14" width="56" height="50" rx="6" fill="var(--orange)"/><path d="M56 32l26-16v46L56 46z" fill="var(--orange)"/></svg>
    <h3>Filmmaker</h3>
    <p>Temporibus autem quibusdam et aut officiis deb itis aut re rum necessitatibus saepe eveniet ut vo luptates repuian dae sint et molestiae non rcusa ndae nostrum exerci.</p>
  </div>
  <div class="abs skill" style="left:793px">
    <svg class="icon" width="60" height="80" viewBox="0 0 60 80"><circle cx="30" cy="28" r="24" fill="none" stroke="var(--orange)" stroke-width="6"/><rect x="20" y="52" width="20" height="12" fill="var(--orange)"/><rect x="22" y="66" width="16" height="5" fill="var(--orange)"/><rect x="25" y="73" width="10" height="4" fill="var(--orange)"/></svg>
    <h3>Entrepreneur</h3>
    <p>Temporibus autem quibusdam et aut officiis deb itis aut re rum necessitatibus saepe eveniet ut vo luptates repuian dae sint et molestiae non rcusa ndae nostrum exerci.</p>
  </div>
</section>

<footer class="footer">
  <div class="abs social">
    <span>Chirp</span><span>Netwk</span><span>Repo</span>
    <span><svg width="20" height="14" viewBox="0 0 20 14"><rect x="1" y="1" width="18" height="12" rx="2" fill="#fff"/><path d="M1 2l9 6 9-6" fill="none" stroke="#161616" stroke-width="1.5"/></svg></span>
  </div>
  <div class="abs contact center">
    <svg width="10" height="14" viewBox="0 0 10 14"><path d="M5 0a5 5 0 0 1 5 5c0 4-5 9-5 9S0 9 0 5a5 5 0 0 1 5-5z" fill="#ddd"/><circle cx="5" cy="5" r="2" fill="#161616"/></svg>
    Larkspur Lane 14, 4021 Brenmoor &nbsp;|&nbsp;
    <svg width="13" height="13" viewBox="0 0 13 13"><path d="M2 1l3 0 1 3-2 1.5a8 8 0 0 0 3.5 3.5L9 7l3 1v3c-6 1-11-4-10-10z" fill="#ddd"/></svg>
    1 555 010 2040 &nbsp;|&nbsp;
    <svg width="14" height="10" viewBox="0 0 14 10"><rect width="14" height="10" rx="1" fill="#ddd"/><path d="M0 1l7 5 7-5" fill="none" stroke="#161616"/></svg>
    hello@daneholpvist.com
  </div>
  <div class="abs links center">Help &nbsp;&nbsp;|&nbsp;&nbsp; FAQ &nbsp;&nbsp;|&nbsp;&nbsp; Support &nbsp;&nbsp;|&nbsp;&nbsp; Sitemap &nbsp;&nbsp;|&nbsp;&nbsp; Terms Of Use &nbsp;&nbsp;|&nbsp;&nbsp; Privacy Statement</div>
  <div class="abs copy center">Copyrights © 2018, Dane Holpvist. All rights reserved.</div>
</footer>

</body>
</html>
```